Holloway Photography.
I really don't know what should go here
Simple
Glen Holloway
Owner
4820 NE Corvel Dr Ankeny Ia 50023
holloway.photography@brevanmail.com
hollowayphotography.net
I am thinking that i will put a photo, or just my logo on one side, and the rest of the info on the other.
This is one of those moments...
let us tell your story.

```html
<!DOCTYPE html>
<html lang="en">
<head>
<meta charset="utf-8">
<title>Holloway Photography – Business Card</title>
<link href="https://fonts.googleapis.com/css2?family=Marcellus+SC&family=Open+Sans:wght@400;600&display=swap" rel="stylesheet">
<style>
  :root{
    --stage:#3a2e2a;
    --card-dark:#141414;
    --card-mid:#3a3a3a;
    --ink:#f2f2f2;
    --ink-soft:#bdbdbd;
    --rule:#8a8a8a;
    --stripe:#e9e9e9;
  }
  *{margin:0;padding:0;box-sizing:border-box}
  html,body{width:1200px;height:456px;overflow:hidden;background:var(--stage)}
  .stage{position:relative;width:1200px;height:456px}
  .card{position:absolute;top:93px;width:450px;height:270px;overflow:hidden;
        box-shadow:0 4px 14px rgba(0,0,0,.55)}
  .card--front{left:137px;background:radial-gradient(ellipse at 45% 35%,var(--card-mid),var(--card-dark) 75%)}
  .card--back{left:612px;background:radial-gradient(ellipse at 50% 45%,#4a4a4a,var(--card-dark) 80%)}

  .edge-stripes{position:absolute;left:22px;top:0;width:30px;height:270px}
  .edge-stripes span{position:absolute;left:0;width:30px;background:var(--stripe)}

  .mark{position:absolute;display:flex;flex-direction:column;align-items:center;gap:10px;
        font-family:"Marcellus SC",serif;color:var(--ink)}
  .mark__dot{width:40px;height:40px;border-radius:50%;border:2px solid var(--ink)}
  .mark__name{font-size:17px;letter-spacing:.5px;white-space:nowrap}
  .card--front .mark{left:70px;top:38px}

  .address{position:absolute;left:74px;top:146px;font:400 9px/1.5 "Open Sans",sans-serif;color:var(--ink-soft)}
  .person{position:absolute;left:262px;top:146px;font-family:"Marcellus SC",serif;color:var(--ink)}
  .person__name{font-size:19px}
  .person__role{font:400 9px "Open Sans",sans-serif;color:var(--ink-soft);margin-top:2px}

  .contacts{position:absolute;left:74px;top:194px;list-style:none;font:400 9px/1.9 "Open Sans",sans-serif;color:var(--ink-soft)}
  .contacts b{display:inline-block;width:20px;color:var(--ink);font-weight:600}

  .halftone{position:absolute;right:0;bottom:0;width:210px;height:140px;
            background:radial-gradient(ellipse at 100% 100%,rgba(120,120,120,.35),transparent 70%)}

  .backdrop{position:absolute;inset:0;
            background:radial-gradient(ellipse at 48% 40%,rgba(190,190,190,.28),transparent 55%)}
  .card--back .mark{left:0;right:0;top:58px}
  .card--back .mark__dot{width:50px;height:50px}
  .card--back .mark__name{font-size:22px}
  .back-rule{position:absolute;left:20px;right:20px;height:1px;background:var(--rule)}
  .back-rule--top{top:203px}
  .back-rule--bottom{top:222px}
  .back-web{position:absolute;left:95px;top:206px;font:400 9px "Open Sans",sans-serif;color:var(--ink-soft)}
</style>
</head>
<body>
<main class="stage">
  <section class="card card--front">
    <div class="edge-stripes">
      <span style="top:0;height:20px"></span>
      <span style="top:26px;height:14px"></span>
      <span style="top:46px;height:14px"></span>
      <span style="top:66px;height:204px"></span>
    </div>
    <div class="mark">
      <div class="mark__dot"></div>
      <div class="mark__name">Holloway Photography.</div>
    </div>
    <p class="address">4820 NE Corvel Dr Ankeny<br>Ia 50023</p>
    <div class="person">
      <div class="person__name">Glen Holloway</div>
      <div class="person__role">Managing Director</div>
    </div>
    <ul class="contacts">
      <li><b>P</b>515-555-0142</li>
      <li><b>E</b>holloway.photography@brevanmail.com</li>
      <li><b>W</b>www.hollowayphotography.net</li>
    </ul>
    <div class="halftone"></div>
  </section>

  <section class="card card--back">
    <div class="backdrop" role="img" aria-label="Faint monochrome family photograph behind the brand name"></div>
    <div class="mark">
      <div class="mark__dot"></div>
      <div class="mark__name">Holloway Photography.</div>
    </div>
    <div class="back-rule back-rule--top"></div>
    <span class="back-web">www.hollowayphotography.net</span>
    <div class="back-rule back-rule--bottom"></div>
  </section>
</main>
</body>
</html>
```